Roles On Ledger - Job Board for Big Data Professionals

Hi all,

I need a design for a job board I'm kicking off that is focused on finding jobs and people that work in Data Analytics.

I've attached a fairly in depth design spec and wireframe giving a rough mockup. Please note that in the wireframe, the boxes are there to demonstrate orders of content. This is not to say that a lot of distinct content boxes will necessarily be the best way of presenting content.

I will be available on Chatterly (marcus.holloway) and email (h0ll0w4y@quillpost.net) and will give constant and clear feedback on the way.

Payment is not guaranteed yet. As soon as there are at least 5+ promising designs I will make this guaranteed.

Thanks
Marcus
Updates

Hi all

Please suspend all work on this project for the time being.

I am working closely with 1 designer who I will very likely accept their design.

I appreciate all the work you have put into this, but dont want to waste any more of your time.

Thanks
Marcus

Industry/Entity Type

Work

Requirements
Must have
• I'd like a clean, modern web design which has strong use of Typography. Strong use of a clear and consistent palette of colours.
Should not have
• Boxes with rounded edges

```html
<!DOCTYPE html>
<html lang="en">
<head>
<meta charset="utf-8">
<title>Roles On Ledger – Job Board</title>
<link href="https://fonts.googleapis.com/css2?family=Arimo:wght@400;700&family=PT+Serif:wght@400;700&family=Open+Sans:wght@400&family=Oswald:wght@500;700&family=Cinzel&display=swap" rel="stylesheet">
<style>
:root{
  --header-dark:#2c2c2c;
  --footer-dark:#2a2a2a;
  --panel:#474747;
  --page:#e6e6e6;
  --white:#ffffff;
  --blue:#2b8fdb;
  --blue-light:#4eb6ea;
  --nav-top:#45a8ee;
  --nav-bottom:#1c7ccd;
  --nav-active:#1566b0;
  --red:#c43b2e;
  --yellow:#f6c41c;
  --text:#5a5a5a;
  --muted:#8a8a8a;
  --rule:#dcdcdc;
  --table-head:#3f3f3f;
}
*{box-sizing:border-box;margin:0;padding:0}
html,body{width:1155px;height:1200px;overflow:hidden}
body{background:var(--page);font-family:"Arimo",Arial,sans-serif;color:var(--text)}
.canvas{position:relative;width:1155px;height:1200px;overflow:hidden}
.abs{position:absolute}

.site-header{position:absolute;left:0;top:0;width:1155px;height:165px;background:var(--header-dark)}
.logo{position:absolute;font-family:"Open Sans",sans-serif;font-weight:400;font-size:40px;color:var(--blue);letter-spacing:-.5px;white-space:nowrap}
.logo.is-footer{font-size:36px}
.ad-space{position:absolute;left:610px;top:21px;width:466px;height:60px;background:linear-gradient(#ffffff,#d9d9d9);border:2px solid #bdbdbd;display:flex;align-items:center;justify-content:center;font-family:"Cinzel",serif;font-size:36px;color:#b5b5b5;letter-spacing:2px}

.container{position:absolute;left:79px;top:102px;width:997px;height:921px;background:var(--white)}

.main-nav{position:absolute;left:79px;top:102px;width:997px;height:37px;background:linear-gradient(var(--nav-top),var(--nav-bottom))}
.main-nav a{position:absolute;top:0;height:37px;line-height:37px;font-family:"PT Serif",serif;font-weight:700;font-size:16px;color:var(--white);text-decoration:none;white-space:nowrap}
.main-nav .is-home{background:var(--nav-active);padding:0 23px}
.main-nav .is-current{background:var(--white);color:#333;padding:0 17px;top:-2px;height:39px}
.sub-nav{position:absolute;left:79px;top:139px;width:997px;height:29px;background:linear-gradient(#fafafa,#e2e2e2);border-bottom:1px solid #cfcfcf}
.sub-nav a{position:absolute;top:0;line-height:29px;font-family:"PT Serif",serif;font-size:13px;color:#333;text-decoration:none;white-space:nowrap}

.hero{position:absolute;left:96px;top:185px;width:963px;height:303px;background:var(--panel)}
.hero-title{position:absolute;font-family:"PT Serif",serif;font-weight:700;font-size:21px;color:#c9c9c9}
.field{position:absolute;height:23px;background:linear-gradient(#ffffff,#e9e9e9);border:1px solid #bbb;font-size:12px;color:#999;padding-left:8px;line-height:21px}
.btn-blue{position:absolute;background:linear-gradient(#3d9fe8,#1a73c2);color:#fff;font-weight:700;font-size:14px;text-align:center}
.hero-note{position:absolute;font-size:11px;color:#eee;white-space:nowrap}
.type-label{position:absolute;font-family:"PT Serif",serif;font-weight:700;font-size:16px;color:#fff}
.radio{position:absolute;display:flex;align-items:center;gap:5px;font-size:12px;color:#fff}
.radio i{display:inline-block;width:14px;height:14px;border-radius:50%;background:#fff;border:1px solid #999}
.radio i.on{background:radial-gradient(circle,var(--blue) 40%,#fff 45%)}
.btn-yellow{position:absolute;left:310px;top:432px;width:73px;height:23px;background:linear-gradient(#ffd84a,#f0b400);color:#6a4a00;font-size:14px;text-align:center;line-height:23px}
.adv-link{position:absolute;left:396px;top:434px;font-family:"PT Serif",serif;font-size:12px;color:#eee}

.news-card{position:absolute;left:503px;top:177px;width:282px;height:318px;background:#f7f7f7;box-shadow:0 0 8px rgba(0,0,0,.5)}
.card-title{position:absolute;font-family:"PT Serif",serif;font-weight:700;font-size:14px;color:#444}
.more-link{position:absolute;right:12px;top:21px;font-size:11px;color:var(--red);text-decoration:underline}
.news-list{position:absolute;left:14px;top:50px;width:256px;list-style:none}
.news-list li{position:relative;height:26.5px;line-height:26.5px;padding-left:24px;font-size:11px;color:#666;border-bottom:1px dotted #d2d2d2}
.news-list li::before,.bullet-list li::before{content:"";position:absolute;left:4px;top:50%;width:9px;height:9px;margin-top:-4.5px;border-radius:50%;background:var(--red)}
.card-rule{position:absolute;left:14px;width:256px;border-top:1px solid #d5d5d5}
.card-text{position:absolute;font-size:11px;color:#666;white-space:nowrap}
.email-label{position:absolute;left:14px;top:247px;font-weight:700;font-size:14px;color:var(--blue)}
.btn-dark{position:absolute;left:566px;top:452px;width:79px;height:25px;background:linear-gradient(#666,#3a3a3a);color:#fff;font-weight:700;font-size:13px;text-align:center;line-height:25px}

.resume-btn{position:absolute;left:825px;top:211px;width:211px;height:53px;border-radius:27px;background:linear-gradient(#ffe35a,#f2b100);border:3px solid #fff3c0;display:flex;align-items:center;justify-content:center;font-family:"Oswald",sans-serif;font-weight:700;font-size:22px;color:var(--red);letter-spacing:.5px}
.select{position:absolute;left:805px;top:320px;width:235px;height:33px;background:linear-gradient(#e2e2e2,#c6c6c6);border:1px solid #888;font-size:17px;color:#555;line-height:31px;padding-left:10px}
.select-arrow{position:absolute;right:0;top:0;width:22px;height:31px;background:#3b3b3b}
.grad-btn{position:absolute;left:808px;top:389px;width:227px;height:66px;background:linear-gradient(#4fb3f5,#1a6fc5);border:2px solid #9ad3fa;display:flex;align-items:center;justify-content:center;font-family:"Oswald",sans-serif;font-weight:700;font-size:36px;color:#fff;letter-spacing:1px}

.section-title{position:absolute;font-family:"PT Serif",serif;font-weight:700;font-size:15px;color:#333;white-space:nowrap}
.body-copy{position:absolute;font-size:12.4px;line-height:19.8px;color:#666}
.dotted-rule{position:absolute;border-top:1px dotted #bbb}
.col-head{position:absolute;font-weight:700;font-size:13px;color:var(--blue)}
.bullet-list{position:absolute;list-style:none}
.bullet-list li{position:relative;height:22px;line-height:22px;padding-left:22px;font-size:11.5px;color:#666;white-space:nowrap}

.tweet-icon{position:absolute;left:808px;top:513px;width:32px;height:32px;border-radius:50%;background:var(--blue-light)}
.tweet-box{position:absolute;left:804px;top:548px;width:255px;height:107px;background:var(--blue-light);padding:11px 13px;font-size:11.5px;line-height:18px;color:#fff}
.tweet-box em{display:block;font-size:11px;color:#e8f6ff}

.cat-head{position:absolute;height:28px;background:var(--table-head);color:#fff;font-family:"PT Serif",serif;font-weight:700;font-size:12.5px}
.cat-head span{position:absolute;top:0;line-height:28px}
.cat-list{position:absolute;list-style:none}
.cat-list li{position:relative;height:21.5px;line-height:21.5px;padding-left:22px;font-size:11.5px;color:#555;white-space:nowrap}
.cat-list li::before{content:"";position:absolute;left:4px;top:50%;width:9px;height:9px;margin-top:-4.5px;border-radius:50%;background:var(--red)}
.cat-list li.view-all{font-size:11px;color:#333;text-decoration:underline;text-decoration-color:var(--red)}
.cat-list li.view-all::before{display:none}

.partners{position:absolute;left:804px;top:681px;width:254px;height:309px;border:1px solid #cfcfcf;background:#fff;display:grid;grid-template-columns:repeat(3,1fr);grid-template-rows:repeat(8,1fr);gap:6px;padding:8px}
.partner{background:#ccc}

.site-footer{position:absolute;left:0;top:1023px;width:1155px;height:177px;background:var(--footer-dark)}
.foot-title{position:absolute;font-family:"PT Serif",serif;font-weight:700;font-size:16px;color:var(--blue);white-space:nowrap}
.foot-list{position:absolute;list-style:none;border-left:1px solid #777}
.foot-list li{position:relative;height:27.5px;line-height:27.5px;padding-left:14px;font-size:12px;color:#cfcfcf;white-space:nowrap}
.foot-list li::before{content:"";position:absolute;left:0;top:50%;width:9px;border-top:1px solid #777}
.social{position:absolute;display:flex;align-items:center;gap:8px;font-size:12px;color:#ddd;white-space:nowrap}
.social i{display:inline-block;width:15px;height:15px}
.copyright{position:absolute;right:99px;top:1137px;font-size:11.5px;color:#ccc;text-align:right}
</style>
</head>
<body>
<div class="canvas">

  <header class="site-header">
    <div class="logo" style="left:102px;top:20px">Roles On Ledger</div>
    <div class="ad-space">Ad Space</div>
  </header>

  <div class="container"></div>

  <nav class="main-nav">
    <a class="is-home" style="left:0">Home</a>
    <a style="left:107px">About Us</a>
    <a class="is-current" style="left:195px">Jobs</a>
    <a style="left:292px">Account</a>
    <a style="left:391px">Register</a>
    <a style="left:492px">News &amp; Insight</a>
    <a style="left:645px">Graduates</a>
    <a style="left:761px">Recruiters</a>
  </nav>
  <nav class="sub-nav">
    <a style="left:23px">Advanced Job Search</a>
    <a style="left:169px">Companies</a>
    <a style="left:261px">Account</a>
    <a style="left:338px">Login</a>
    <a style="left:401px">Post Resume</a>
    <a style="left:502px">Alerts</a>
    <a style="left:566px">Settings</a>
  </nav>

  <section class="hero">
    <div class="hero-title" style="left:16px;top:14px">Login</div>
    <div class="field" style="left:16px;top:64px;width:178px">Username</div>
    <div class="field" style="left:209px;top:64px;width:182px">Password</div>
    <div class="btn-blue" style="left:16px;top:104px;width:74px;height:23px;line-height:23px">Sign In</div>
    <div class="hero-note" style="left:98px;top:109px">Forgot your password ?</div>
    <div class="hero-title" style="left:16px;top:146px">Quick Search</div>
    <div class="field" style="left:16px;top:201px;width:178px">Keyword</div>
    <div class="field" style="left:209px;top:201px;width:182px">Location</div>
    <div class="type-label" style="left:16px;top:233px">Type</div>
    <div class="radio" style="left:16px;top:255px"><i class="on"></i>Contract</div>
    <div class="radio" style="left:88px;top:255px"><i></i>Permanent</div>

    <svg class="abs" style="left:697px;top:22px" width="38" height="60" viewBox="0 0 38 60" aria-hidden="true">
      <path d="M34 4 C8 8 2 32 22 54" fill="none" stroke="#fff" stroke-width="3"/>
      <path d="M14 50 L23 56 L25 45" fill="none" stroke="#fff" stroke-width="3"/>
    </svg>
    <div class="hero-note" style="left:757px;top:95px">Click here and post your resume</div>
  </section>
  <div class="btn-yellow">Search</div>
  <div class="adv-link">Advanced Search</div>

  <section class="news-card">
    <div class="card-title" style="left:14px;top:17px">Latest News</div>
    <div class="more-link">More articles</div>
    <ul class="news-list">
      <li>Your openings are featured in one of the top.</li>
      <li>Your credits are valid for unlimited time</li>
      <li>You can change your job postings you like</li>
      <li>Job postings are online immediately</li>
    </ul>
    <div class="card-rule" style="top:177px"></div>
    <div class="card-title" style="left:14px;top:184px">Subscribe For Job Alerts</div>
    <div class="card-rule" style="top:212px"></div>
    <div class="card-text" style="left:14px;top:218px">Lorem Ipsum is simply dummy text of the printing.</div>
    <div class="email-label">Email</div>
    <div class="field" style="left:63px;top:242px;width:198px;height:25px"></div>
  </section>
  <div class="btn-dark">Submit</div>

  <div class="resume-btn">POST YOUR RESUME</div>
  <div class="select">Recruiters<span class="select-arrow"></span></div>
  <div class="grad-btn">GRADUATES</div>

  <div class="section-title" style="left:96px;top:520px">Welcome to Roles On Ledger</div>
  <p class="body-copy" style="left:96px;top:551px;width:390px">Lorem Ipsum is simply dummy text of the printing and typesetting industry. Lorem Ipsum has been the industry's standard dummy text ever since the 1500s, when an unknown printer took a galley of type and scrambled it to make a type specimen book. It has survived not only five centuries, but also the leap into electronic typesetting.</p>

  <div class="section-title" style="left:503px;top:520px">Why Roles On Ledger?</div>
  <div class="dotted-rule" style="left:503px;top:545px;width:282px"></div>
  <div class="col-head" style="left:513px;top:552px">Jobseekers</div>
  <div class="col-head" style="left:660px;top:552px">Recruiters</div>
  <ul class="bullet-list" style="left:508px;top:570px">
    <li>Browse Jobs</li><li>Job Search</li><li>Register Now</li>
  </ul>
  <ul class="bullet-list" style="left:655px;top:570px">
    <li>Login</li><li>Advertise</li><li>Search Resumes</li>
  </ul>

  <div class="tweet-icon"></div>
  <div class="section-title" style="left:844px;top:520px">Latest from @Chirpline</div>
  <div class="tweet-box">chirpline Our #YearInReview finale: The 2011 Golden ChirpAward goes to @Maplecrumb chp.ln/r8Kt2mPa chp.ln/Vq3nXe7D<em>Posted 5 days ago</em></div>

  <div class="section-title" style="left:96px;top:658px">Job Categories</div>
  <div class="cat-head" style="left:96px;top:686px;width:693px">
    <span style="left:10px">Industries</span><span style="left:260px">Location</span><span style="left:458px">Functional Area</span>
  </div>
  <ul class="cat-list" style="left:100px;top:716px">
    <li>IT - Software Jobs (9843)</li><li>Manufacturing Jobs (3441)</li><li>Education / Training Jobs (2396)</li><li>BPO / Call Center Jobs (2367)</li><li class="view-all">view all</li>
  </ul>
  <ul class="cat-list" style="left:351px;top:716px">
    <li>Delhi Jobs (8637)</li><li>Bangalore Jobs (6517)</li><li>Mumbai Jobs (5233)</li><li>Gurgaon Jobs (4102)</li><li class="view-all">view all</li>
  </ul>
  <ul class="cat-list" style="left:549px;top:716px">
    <li>General / Other Software Jobs (5616)</li><li>Sales / BD Jobs (5488)</li><li>Finance / Accounts / Tax Jobs (2179)</li><li>Engineering Design Jobs (1499)</li><li class="view-all">view all</li>
  </ul>

  <div class="cat-head" style="left:96px;top:838px;width:693px">
    <span style="left:10px">Functional Area</span><span style="left:260px">Popular Jobs</span><span style="left:458px">Industries</span>
  </div>
  <ul class="cat-list" style="left:100px;top:872px">
    <li>General / Other Software Jobs (5616)</li><li>Sales / BD Jobs (5488)</li><li>Finance / Accounts / Tax Jobs (2179)</li><li>Engineering Design Jobs (1499)</li><li class="view-all">view all</li>
  </ul>
  <ul class="cat-list" style="left:351px;top:872px">
    <li>Web Developer (0-2 Yr)</li><li>Web Developer (0- 2Yr)</li><li>Assistant /Junior (0-2Yr)</li><li>Telecom Engineer (0-2Yr)</li><li class="view-all">view all</li>
  </ul>
  <ul class="cat-list" style="left:549px;top:872px">
    <li>IT - Software Jobs (9843)</li><li>Manufacturing Jobs (3441)</li><li>Education / Training Jobs (2396)</li><li>BPO / Call Center Jobs (2367)</li><li class="view-all">view all</li>
  </ul>

  <div class="section-title" style="left:804px;top:658px">Featured Partners</div>
  <div class="partners" role="img" aria-label="Grid of featured partner badges">
    <div class="partner" style="background:#e23a6b"></div><div class="partner" style="background:#d9dde3"></div><div class="partner" style="background:#e6eef7"></div>
    <div class="partner" style="background:#3b6fb6"></div><div class="partner" style="background:#c8322d"></div><div class="partner" style="background:#1d4e9a"></div>
    <div class="partner" style="background:#e7e7e7"></div><div class="partner" style="background:#f1e2c9"></div><div class="partner" style="background:#dfe7f2"></div>
    <div class="partner" style="background:#1f2a1f"></div><div class="partner" style="background:#d8e8f3"></div><div class="partner" style="background:#e3ecf6"></div>
    <div class="partner" style="background:#ece6df"></div><div class="partner" style="background:#e4e9f0"></div><div class="partner" style="background:#a4cf3c"></div>
    <div class="partner" style="background:#f3e1d3"></div><div class="partner" style="background:#ececec"></div><div class="partner" style="background:#dfe6f0"></div>
    <div class="partner" style="background:#e9edf1"></div><div class="partner" style="background:#e8e8e8"></div><div class="partner" style="background:#f4e1e1"></div>
    <div class="partner" style="background:#e2e6ea"></div><div class="partner" style="background:#dce8f4"></div><div class="partner" style="background:#eaf1f7"></div>
  </div>

  <footer class="site-footer">
    <div class="foot-title" style="left:96px;top:13px">Browse Company</div>
    <ul class="foot-list" style="left:103px;top:52px"><li>Home</li><li>Jobs</li><li>Account Register</li><li>News &amp; Insight</li></ul>
    <ul class="foot-list" style="left:224px;top:52px"><li>News &amp; Insight</li><li>Graduates</li><li>Recruiters</li><li>About</li></ul>
    <div class="foot-title" style="left:360px;top:13px">Job Seekers</div>
    <ul class="foot-list" style="left:368px;top:52px"><li>Browse Jobs</li><li>Job Search</li><li>Register Now</li><li>Login</li></ul>
    <div class="foot-title" style="left:493px;top:13px">Employers</div>
    <ul class="foot-list" style="left:501px;top:52px"><li>Recruiters</li><li>Post Jobs</li><li>Access Database</li><li>Industries</li></ul>
    <div class="foot-title" style="left:632px;top:13px">Social Sharing</div>
    <div class="social" style="left:635px;top:60px"><i style="background:var(--blue-light)"></i>Follow us on Chirpline</div>
    <div class="social" style="left:635px;top:89px"><i style="background:#f08a1c"></i>Post RSS Feeds</div>
    <div class="logo is-footer" style="left:797px;top:22px">Roles On Ledger</div>
  </footer>
  <div class="copyright">Copyright © 2011 Roles On Ledger.</div>

</div>
</body>
</html>
```